Business Card Design

We need a business card design for a new company. We produce and sell fully grown topiary (please Google topiary pictures if you are not familiar with Topiary).We make many different topiary designs and shapes in all sizes. Ranging from cute little table top animal sculptures such as bunnies and swans for the indoors, to big sculptures such as actual size elephants for outdoor gardens and parks. We also make topiary balls, spiral shapes and other attractive geometrical shapes for indoor and outdoor decorations. We want to see designs that reflects the playfulness and ,liveliness and cute characteristics of our products.Please find attached the logo.Thank you

Industry/Entity Type

Business

Contact Information for Business Card

Company Name : Leaf Forge
Slogan : Shaping Every Garden Bright
Tagline: Topiary...and more
Website : www.leafforge.example

Name on Card : Youssef Nabil Darwish
Title : Founder & CEO
email: youssef_nabil@leafforge.example

Address : 27 El-Masry Street
Ground Floor,Ste.1
El-Marg,Cairo,Egypt

Office Telephone : (02) 25948017
Mobile Number : 01287719462

Requirements
Must have
• The business card must have a white background.

```html
<!DOCTYPE html>
<html lang="en">
<head>
<meta charset="utf-8">
<title>Leaf Forge – Business Card</title>
<link rel="stylesheet" href="https://fonts.googleapis.com/css2?family=Open+Sans:wght@400;600;700&display=swap">
<style>
  :root {
    --bg: #ece6dc;
    --green: #6aa532;
    --green-dark: #5a9328;
    --orange: #e0662a;
    --paper: #f7f6f1;
    --text-light: #ffffff;
    --text-soft: #e6f2d8;
    --line-soft: rgba(255,255,255,0.35);
  }
  * { margin: 0; padding: 0; box-sizing: border-box; }
  html, body { width: 1200px; height: 1023px; overflow: hidden; background: var(--bg); }
  body { font-family: "Open Sans", Arial, sans-serif; position: relative; }

  .card {
    position: absolute; left: 100px; top: 226px;
    width: 1000px; height: 571px;
    background: var(--green);
    overflow: hidden;
    box-shadow: 0 10px 30px rgba(0,0,0,0.18);
  }
  .card__top-band { position: absolute; left: 0; top: 0; width: 100%; height: 70px; background: var(--green); border-bottom: 4px solid var(--orange); }
  .card__brand-band {
    position: absolute; left: 0; top: 74px; width: 100%; height: 226px;
    background: var(--paper);
    border-bottom: 4px solid var(--orange);
    display: flex; flex-direction: column; align-items: center; justify-content: center;
  }
  .brand { display: flex; align-items: center; gap: 14px; }
  .brand__dot { width: 26px; height: 26px; border-radius: 50%; background: var(--green); }
  .brand__name { font-size: 72px; font-weight: 600; color: var(--green); letter-spacing: 1px; line-height: 1; }
  .brand__slogan { margin-top: 14px; font-size: 24px; color: var(--green); font-weight: 400; }

  .card__info-band { position: absolute; left: 0; top: 304px; width: 100%; height: 267px; background: linear-gradient(180deg, var(--green) 0%, var(--green-dark) 100%); }
  .person { position: absolute; left: 70px; top: 150px; color: var(--text-light); }
  .person__name { font-size: 24px; font-weight: 700; text-transform: uppercase; letter-spacing: 0.5px; }
  .person__title { font-size: 18px; color: var(--text-soft); margin-top: 2px; }

  .contacts {
    position: absolute; left: 560px; top: 34px;
    padding-left: 22px; border-left: 1px solid var(--line-soft);
    list-style: none; color: var(--text-light); font-size: 17px;
  }
  .contacts__item { display: flex; align-items: flex-start; gap: 12px; line-height: 1.55; }
  .contacts__item--strong { font-weight: 700; }
  .contacts__icon { width: 16px; height: 16px; margin-top: 5px; flex: none; }
</style>
</head>
<body>
  <article class="card">
    <div class="card__top-band"></div>

    <header class="card__brand-band">
      <div class="brand">
        <span class="brand__dot"></span>
        <span class="brand__name">Leaf Forge</span>
      </div>
      <p class="brand__slogan">Shaping Every Garden Bright</p>
    </header>

    <section class="card__info-band">
      <div class="person">
        <p class="person__name">Youssef Nabil Darwish</p>
        <p class="person__title">Founder &amp; CEO</p>
      </div>

      <ul class="contacts">
        <li class="contacts__item contacts__item--strong">
          <svg class="contacts__icon" viewBox="0 0 16 16"><path fill="#fff" d="M4 1l2.5 3-1.5 2c1 2 3 4 5 5l2-1.5 3 2.5-1.5 2.5C7 15 1 9 1.5 2.5z"/></svg>
          0 128 771 9462
        </li>
        <li class="contacts__item">
          <svg class="contacts__icon" viewBox="0 0 16 16"><path fill="#fff" d="M4 1l2.5 3-1.5 2c1 2 3 4 5 5l2-1.5 3 2.5-1.5 2.5C7 15 1 9 1.5 2.5z"/></svg>
          (02) 25 94 8017
        </li>
        <li class="contacts__item">
          <svg class="contacts__icon" viewBox="0 0 16 16"><g fill="none" stroke="#fff" stroke-width="1.4"><circle cx="8" cy="8" r="6.5"/><ellipse cx="8" cy="8" rx="3" ry="6.5"/><path d="M1.5 8h13"/></g></svg>
          www.leafforge.example
        </li>
        <li class="contacts__item">
          <svg class="contacts__icon" viewBox="0 0 16 16"><rect x="1" y="3" width="14" height="10" fill="#fff"/><path d="M1 3l7 6 7-6" fill="none" stroke="#6aa532" stroke-width="1.3"/></svg>
          youssef_nabil@leafforge.example
        </li>
        <li class="contacts__item">
          <svg class="contacts__icon" viewBox="0 0 16 16"><path fill="#fff" d="M8 0.5a5 5 0 0 1 5 5c0 4-5 10-5 10s-5-6-5-10a5 5 0 0 1 5-5z"/><circle cx="8" cy="5.5" r="1.8" fill="#6aa532"/></svg>
          <span>27 El-Masry Street Ground Floor<br>Ste.1 El-Marg,Cairo,Egypt</span>
        </li>
      </ul>
    </section>
  </article>
</body>
</html>
```